Dravell PowerPoint Theme/Template

I want to be able to put together presentations that have a cohesive look and work with my current branding on my website (www.dravell.com) and social media (#dravellskincare).

```html
<!DOCTYPE html>
<html lang="en">
<head>
<meta charset="utf-8">
<title>Dravell Presentation Theme</title>
<link href="https://fonts.googleapis.com/css2?family=Poppins:wght@400;500;600;700;800&display=swap" rel="stylesheet">
<style>
:root{
  --brown:#9c5a2a;
  --brown-dark:#7d4520;
  --tan:#c58d5a;
  --sand:#e6c3a2;
  --cream:#faf1e8;
  --peach:#f2dcc8;
  --white:#ffffff;
  --ink:#5a3a22;
  --canvas:#e9e9e9;
  --stage:#cfcfcf;
  --skin-a:#e8c4a6;
  --skin-b:#b98564;
  --leaf-a:#4e7a3e;
  --leaf-b:#234a24;
}
*{box-sizing:border-box;margin:0;padding:0}
html,body{width:1200px;height:2924px;overflow:hidden}
body{position:relative;background:var(--canvas);font-family:"Poppins",sans-serif;color:var(--ink)}
.stage{position:absolute;left:0;top:2030px;width:1200px;height:894px;background:var(--stage)}
.slide{position:absolute;width:532px;height:300px;overflow:hidden;background:var(--cream);box-shadow:0 2px 6px rgba(0,0,0,.12)}
.photo{position:absolute;background:linear-gradient(150deg,var(--skin-a),var(--skin-b))}
.photo.leaf{background:linear-gradient(150deg,var(--leaf-a),var(--leaf-b))}
.photo.grass{background:linear-gradient(180deg,#5f8f3c,#2f5a22)}
.blob{position:absolute;border-radius:50%;background:var(--peach)}
.brand{position:absolute;font-weight:700;color:var(--brown);letter-spacing:-.5px;line-height:1}
.brand-sub{position:absolute;font-size:9px;color:var(--brown);font-weight:500}
.title{position:absolute;font-weight:700;color:var(--brown);line-height:1.05}
.copy{position:absolute;font-size:8px;line-height:1.45;color:var(--ink)}
.band{position:absolute;background:var(--brown)}
.pill{position:absolute;background:var(--brown);color:var(--white);font-size:9px;font-weight:600;text-align:center;border-radius:3px;padding:3px 0}
.label{font-size:8px;font-weight:600;color:var(--white)}
.svc{position:absolute;top:222px;width:150px;text-align:center}
.svc svg{display:block;margin:0 auto 4px}
.svc b{display:block;font-size:8px;color:var(--brown)}
.svc span{font-size:7px;color:var(--ink)}
.item{display:flex;gap:6px;align-items:flex-start;margin-bottom:10px}
.item i{flex:0 0 8px;height:8px;border-radius:50%;background:var(--white);margin-top:2px}
.item b{display:block;font-size:8px;color:var(--white)}
.item span{font-size:7px;color:var(--sand)}
.contact{position:absolute;display:flex;align-items:center;gap:6px;font-size:8px}
.contact b{display:block;color:var(--brown);font-size:9px}
.big{transform-origin:0 0}
</style>
</head>
<body>
<div class="stage"></div>

<!-- Row 1 -->
<section class="slide" style="left:56px;top:56px">
  <div class="blob" style="width:260px;height:200px;left:-90px;top:-90px"></div>
  <div class="blob" style="width:240px;height:200px;right:-80px;bottom:-100px"></div>
  <div class="brand" style="left:0;width:532px;text-align:center;top:118px;font-size:46px">Dravell</div>
  <div class="brand-sub" style="left:0;width:532px;text-align:center;top:168px">by dr. lena marlow</div>
</section>

<section class="slide" style="left:612px;top:56px">
  <div class="blob" style="width:240px;height:240px;left:-110px;bottom:-120px"></div>
  <div class="title" style="right:30px;top:22px;font-size:26px">AMAZING RESULTS</div>
  <div class="photo" role="img" aria-label="Portrait showing clean skin" style="left:40px;top:80px;width:130px;height:160px;border-radius:8px"></div>
  <div class="photo" role="img" aria-label="Portrait showing soft skin" style="left:196px;top:80px;width:130px;height:160px;border-radius:8px"></div>
  <div class="photo" role="img" aria-label="Portrait showing even skin tone" style="left:352px;top:80px;width:130px;height:160px;border-radius:8px"></div>
  <div class="pill" style="left:55px;top:228px;width:100px">Clean skin</div>
  <div class="pill" style="left:211px;top:228px;width:100px">Soft skin</div>
  <div class="pill" style="left:367px;top:228px;width:100px">Best tone</div>
</section>

<!-- Row 2 -->
<section class="slide" style="left:56px;top:380px">
  <div class="band" style="right:0;top:0;width:120px;height:300px;background:var(--tan)"></div>
  <div class="brand" style="left:28px;top:28px;font-size:28px">Dravell</div>
  <div class="brand-sub" style="left:30px;top:58px">by dr. lena marlow</div>
  <div class="title" style="left:28px;top:110px;font-size:20px">ABOUT DR. MARLOW<br>MD, FAAD</div>
  <div class="copy" style="left:28px;top:170px;width:210px">Board certified dermatologist focused on gentle, science led care for every skin type.</div>
  <div class="photo" role="img" aria-label="Portrait of Dr. Lena Marlow" style="left:290px;top:40px;width:220px;height:220px;border-radius:50%;border:8px solid var(--white)"></div>
</section>

<section class="slide" style="left:612px;top:380px">
  <div class="brand" style="left:26px;top:24px;font-size:28px">Dravell</div>
  <div class="brand-sub" style="left:28px;top:54px">by dr. lena marlow</div>
  <div class="title" style="left:26px;top:110px;font-size:30px">Before &amp;<br>After</div>
  <div class="band" style="left:0;bottom:0;width:266px;height:46px"></div>
  <div class="label" style="position:absolute;left:26px;bottom:16px;font-size:10px">Get the best product</div>
  <div class="photo" role="img" aria-label="Before and after portrait of treated skin" style="left:266px;top:0;width:266px;height:300px"></div>
</section>

<!-- Row 3 -->
<section class="slide" style="left:56px;top:704px">
  <div class="photo" role="img" aria-label="Sunscreen applied to skin" style="left:0;top:0;width:170px;height:150px"></div>
  <div class="photo" role="img" aria-label="Exfoliating product in use" style="left:0;top:150px;width:170px;height:150px;background:linear-gradient(150deg,#f1e4d8,#c9a58a)"></div>
  <div class="label" style="position:absolute;left:16px;top:118px">Balancing sunscreen</div>
  <div class="label" style="position:absolute;left:16px;top:268px">Advanced exfoliation</div>
  <div class="brand" style="left:188px;top:36px;font-size:26px">Dravell</div>
  <div class="brand-sub" style="left:190px;top:64px">by dr. lena marlow</div>
  <div class="photo" role="img" aria-label="Skincare product bottle" style="left:190px;top:110px;width:130px;height:160px;border-radius:6px;background:linear-gradient(150deg,#f7ede4,#d8b99d)"></div>
  <div class="band" style="right:0;top:0;width:192px;height:300px">
    <div class="title" style="left:20px;top:30px;font-size:20px;color:var(--white)">Our Best<br>Products</div>
    <div style="position:absolute;left:20px;top:110px;width:160px">
      <div class="item"><i></i><div><b>Hydrating day cream</b><span>Light, fast absorbing formula</span></div></div>
      <div class="item"><i></i><div><b>Gentle foam cleanser</b><span>Light, fast absorbing formula</span></div></div>
      <div class="item"><i></i><div><b>Renewing night serum</b><span>Light, fast absorbing formula</span></div></div>
    </div>
  </div>
</section>

<section class="slide" style="left:612px;top:704px;background:var(--white)">
  <div class="photo" role="img" aria-label="Woman looking at her skin in a mirror" style="left:0;top:0;width:300px;height:160px"></div>
  <div class="photo" role="img" aria-label="Portrait with green plants" style="left:300px;top:0;width:232px;height:160px;background:linear-gradient(150deg,#d9c7b4,#7f9a6e)"></div>
  <div class="band" style="left:0;top:160px;width:532px;height:40px;background:var(--peach)"></div>
  <div class="title" style="left:0;width:532px;text-align:center;top:171px;font-size:18px">OUR SERVICES</div>
  <div class="svc" style="left:25px">
    <svg width="22" height="22" viewBox="0 0 22 22"><circle cx="11" cy="11" r="10" fill="none" stroke="var(--brown)" stroke-width="1.5"/><path d="M6 11l3.5 3.5L16 8" fill="none" stroke="var(--brown)" stroke-width="1.8"/></svg>
    <b>Skin Care Advice</b><span>Tailored routines for you</span></div>
  <div class="svc" style="left:191px">
    <svg width="22" height="22" viewBox="0 0 22 22"><path d="M11 2C8 7 5 10 5 14a6 6 0 0 0 12 0c0-4-3-7-6-12z" fill="none" stroke="var(--brown)" stroke-width="1.5"/></svg>
    <b>Best skin products</b><span>Tailored routines for you</span></div>
  <div class="svc" style="left:357px">
    <svg width="22" height="22" viewBox="0 0 22 22"><rect x="3" y="3" width="16" height="16" rx="3" fill="none" stroke="var(--brown)" stroke-width="1.5"/><path d="M11 7v8M7 11h8" stroke="var(--brown)" stroke-width="1.8"/></svg>
    <b>Clinic treatments</b><span>Tailored routines for you</span></div>
</section>

<!-- Row 4 -->
<section class="slide" style="left:56px;top:1028px">
  <div class="photo" role="img" aria-label="Smiling woman with glowing skin" style="left:0;top:0;width:266px;height:300px;background:linear-gradient(150deg,#a8724d,#5e3820)"></div>
  <div class="brand" style="left:292px;top:36px;font-size:28px">Dravell</div>
  <div class="brand-sub" style="left:294px;top:66px">by dr. lena marlow</div>
  <div class="title" style="left:292px;top:112px;font-size:26px">Why we are<br>The best</div>
  <div class="copy" style="left:292px;top:184px;width:200px">We blend medical expertise with clean formulas for visible, lasting results.</div>
</section>

<section class="slide" style="left:612px;top:1028px">
  <div class="photo" role="img" aria-label="Portrait touching face" style="left:0;top:0;width:178px;height:150px"></div>
  <div class="photo" role="img" aria-label="Portrait with clear skin" style="left:0;top:150px;width:178px;height:150px;background:linear-gradient(150deg,#f0d6c2,#c59a7c)"></div>
  <div class="brand" style="left:196px;top:36px;font-size:24px">Dravell</div>
  <div class="brand-sub" style="left:198px;top:62px">by dr. lena marlow</div>
  <div class="title" style="left:196px;top:88px;font-size:26px">Best<br>Results</div>
  <div class="photo" role="img" aria-label="Portrait with radiant skin" style="left:178px;top:168px;width:176px;height:132px;background:linear-gradient(150deg,#ecd0ba,#b9886a)"></div>
  <div class="photo" role="img" aria-label="Smiling portrait" style="left:354px;top:0;width:178px;height:300px;background:linear-gradient(150deg,#b77e58,#6b4028)"></div>
</section>

<!-- Row 5 -->
<section class="slide" style="left:56px;top:1352px">
  <div class="photo" role="img" aria-label="Woman with glowing skin" style="left:0;top:0;width:230px;height:300px;background:linear-gradient(150deg,#f0dccb,#c49a7b)"></div>
  <div class="band" style="left:0;top:170px;width:230px;height:130px;background:var(--tan)"></div>
  <div class="title" style="left:20px;top:196px;font-size:22px;color:var(--white)">Know more<br>about your skin</div>
  <div class="brand" style="left:250px;top:40px;font-size:34px">Dravell</div>
  <div class="brand-sub" style="left:252px;top:76px">by dr. lena marlow</div>
  <div class="photo leaf" role="img" aria-label="Green tropical leaf" style="left:330px;top:112px;width:202px;height:188px"></div>
</section>

<section class="slide" style="left:612px;top:1352px">
  <div class="brand" style="left:26px;top:34px;font-size:28px">Dravell</div>
  <div class="brand-sub" style="left:28px;top:64px">by dr. lena marlow</div>
  <div class="title" style="left:26px;top:118px;font-size:28px">For you &amp;<br>your skin</div>
  <div class="photo" role="img" aria-label="Woman holding skincare product" style="left:250px;top:0;width:140px;height:150px"></div>
  <div class="photo leaf" role="img" aria-label="Green leaves" style="left:390px;top:0;width:142px;height:150px"></div>
  <div class="photo" role="img" aria-label="Portrait with warm skin tone" style="left:250px;top:150px;width:140px;height:150px;background:linear-gradient(150deg,#c08a62,#7a4a2c)"></div>
  <div class="photo" role="img" aria-label="Serum dropper bottle" style="left:390px;top:150px;width:142px;height:150px;background:linear-gradient(150deg,#f4ece4,#cfb59c)"></div>
</section>

<!-- Row 6 -->
<section class="slide" style="left:56px;top:1676px;background:var(--white)">
  <div class="photo grass" role="img" aria-label="Fresh green grass" style="left:0;top:0;width:532px;height:190px"></div>
  <div class="title" style="left:0;width:532px;text-align:center;top:72px;font-size:38px;color:var(--white)">Contact Us</div>
  <div class="contact" style="left:40px;top:212px">
    <svg width="22" height="22" viewBox="0 0 22 22"><rect width="22" height="22" rx="4" fill="var(--brown)"/><path d="M7 5l2.5 0 1 3-1.5 1a7 7 0 0 0 3.5 3.5l1-1.5 3 1V14.5c0 1-1 2-2 1.8A10 10 0 0 1 5.2 7C5 6 6 5 7 5z" fill="var(--white)"/></svg>
    <div><b>Phone</b>+1 555 204 8812</div></div>
  <div class="contact" style="left:290px;top:212px">
    <svg width="22" height="22" viewBox="0 0 22 22"><rect width="22" height="22" rx="4" fill="var(--brown)"/><rect x="5" y="7" width="12" height="9" fill="none" stroke="var(--white)" stroke-width="1.4"/><path d="M5 7l6 5 6-5" fill="none" stroke="var(--white)" stroke-width="1.4"/></svg>
    <div><b>E-mail</b>hello@dravell.com</div></div>
  <div class="brand" style="left:0;width:532px;text-align:center;top:266px;font-size:18px">Dravell</div>
</section>

<section class="slide" style="left:612px;top:1676px">
  <div class="blob" style="width:240px;height:200px;left:-80px;top:-100px"></div>
  <div class="blob" style="width:260px;height:200px;right:-100px;bottom:-90px"></div>
  <div class="brand" style="left:0;width:532px;text-align:center;top:86px;font-size:28px">Dravell</div>
  <div class="brand-sub" style="left:0;width:532px;text-align:center;top:116px">by dr. lena marlow</div>
  <div class="title" style="left:0;width:532px;text-align:center;top:146px;font-size:44px">Thank you</div>
</section>

<!-- Featured slides -->
<section class="slide big" style="left:392px;top:2110px;transform:scale(1.35)">
  <div class="blob" style="width:260px;height:200px;left:-90px;top:-90px"></div>
  <div class="blob" style="width:240px;height:200px;right:-80px;bottom:-100px"></div>
  <div class="brand" style="left:0;width:532px;text-align:center;top:118px;font-size:46px">Dravell</div>
  <div class="brand-sub" style="left:0;width:532px;text-align:center;top:168px">by dr. lena marlow</div>
</section>

<section class="slide big" style="left:72px;top:2440px;transform:scale(.95)">
  <div class="photo" role="img" aria-label="Woman with glowing skin" style="left:0;top:0;width:230px;height:300px;background:linear-gradient(150deg,#f0dccb,#c49a7b)"></div>
  <div class="band" style="left:0;top:170px;width:230px;height:130px;background:var(--tan)"></div>
  <div class="title" style="left:20px;top:196px;font-size:22px;color:var(--white)">Know more<br>about your skin</div>
  <div class="brand" style="left:250px;top:40px;font-size:34px">Dravell</div>
  <div class="brand-sub" style="left:252px;top:76px">by dr. lena marlow</div>
  <div class="photo leaf" role="img" aria-label="Green tropical leaf" style="left:330px;top:112px;width:202px;height:188px"></div>
</section>
</body>
</html>
```